Tamburetti, the Postcard Café is looking for new postcards.

Tamburetti sells loads of cards and is always looking for new designs. After three years of selling cards produced by others we are now ready to start our own collection.

What is Tamburetti?
Tamburetti is a place where you, while drinking coffee or tea, can choose a postcard (we have 300 to 400 different kinds for you to choose from), write it, and have it send on any day you want. We are located in the beautiful city of Leiden, The Netherlands. See enclosed document for more info.

What are we looking for?
Funny, witty, colorful designs that make people smile or think. We are thinking to start out with at least 10 different designs.

The dimensions of the cards are 10 x 14,8 cm, either landscape or portrait. Please enter your design in both pdf and original format (ai. psd. or id. file) where possible in vector.

Designs that are offensive to whatever group of people will be removed immediately.

What's in it for you?
You will become part of the Tamburetti collection which you can prove because your name will be on the back of the card.
Furthermore we will pay you € 125,- per chosen postcard.

```html
<!DOCTYPE html>
<html lang="en">
<head>
<meta charset="utf-8">
<title>Ride a Tandem – Bucketlist Postcard No 18</title>
<link rel="stylesheet" href="https://fonts.googleapis.com/css2?family=Kaushan+Script&family=Open+Sans:wght@700;800&display=swap">
<style>
  :root {
    --sky: #6f9aae;
    --ink: #0b0b0b;
    --paper: #ffffff;
    --sprig: #3d5560;
    --bike: #22323a;
  }
  html, body {
    margin: 0;
    padding: 0;
    overflow: hidden;
    background: var(--sky);
  }
  .postcard {
    position: relative;
    width: 811px;
    height: 1200px;
    background: var(--sky);
    overflow: hidden;
  }
  .postcard__frame {
    position: absolute;
    inset: 0;
  }
  .headline {
    position: absolute;
    left: 0;
    width: 811px;
    margin: 0;
    text-align: center;
    font-family: "Kaushan Script", cursive;
    font-weight: 400;
    color: var(--ink);
    text-shadow: 3px 3px 0 var(--paper);
    line-height: 1;
    white-space: nowrap;
  }
  .headline--ride   { top: 203px; font-size: 135px; letter-spacing: 1px; }
  .headline--a      { top: 345px; font-size: 70px; }
  .headline--tandem { top: 399px; font-size: 145px; left: -10px; }
  .banner__label {
    position: absolute;
    top: 599px;
    left: 0;
    width: 811px;
    margin: 0;
    text-align: center;
    font-family: "Open Sans", sans-serif;
    font-weight: 700;
    font-size: 20px;
    letter-spacing: 1.5px;
    color: var(--paper);
  }
  .badge__label {
    position: absolute;
    left: 374px;
    top: 1040px;
    width: 60px;
    margin: 0;
    text-align: center;
    font-family: "Open Sans", sans-serif;
    font-weight: 800;
    font-size: 21px;
    line-height: 23px;
    color: var(--paper);
  }
</style>
</head>
<body>
<main class="postcard">
  <svg class="postcard__frame" width="811" height="1200" viewBox="0 0 811 1200">
    <defs>
      <polygon id="star" points="0,-14 4.1,-4.5 14,-4.3 6.3,2.1 8.8,11.8 0,6.2 -8.8,11.8 -6.3,2.1 -14,-4.3 -4.1,-4.5"/>
    </defs>

    <g class="star-arc" fill="var(--ink)">
      <use href="#star" x="290" y="156"/>
      <use href="#star" x="340" y="123"/>
      <use href="#star" x="403" y="107"/>
      <use href="#star" x="470" y="123"/>
      <use href="#star" x="518" y="156"/>
    </g>

    <ellipse class="laurel laurel--left" cx="240" cy="345" rx="58" ry="20"
             transform="rotate(40 240 345)" fill="var(--sprig)"
             role="img" aria-label="Laurel sprig ornament, left"/>
    <ellipse class="laurel laurel--right" cx="571" cy="345" rx="58" ry="20"
             transform="rotate(-40 571 345)" fill="var(--sprig)"
             role="img" aria-label="Laurel sprig ornament, right"/>

    <path class="headline-swash" d="M385 362 Q410 355 433 351" stroke="var(--ink)" stroke-width="5" fill="none" stroke-linecap="round"/>

    <g class="banner">
      <polygon points="173,630 210,622 210,662 186,668 196,646" fill="var(--ink)" stroke="var(--paper)" stroke-width="2"/>
      <polygon points="640,630 603,622 603,662 627,668 617,646" fill="var(--ink)" stroke="var(--paper)" stroke-width="2"/>
      <path d="M200 600 Q406 578 614 600 L614 646 Q406 624 200 646 Z" fill="var(--ink)"/>
      <path d="M200 650 Q406 628 614 650" stroke="var(--paper)" stroke-width="3" fill="none"/>
    </g>

    <rect class="bicycle" x="60" y="700" width="700" height="307" rx="140"
          fill="var(--bike)" role="img" aria-label="Illustration of a vintage tandem bicycle in black silhouette"/>

    <g class="badge">
      <path d="M233 1067 Q300 1060 367 1065 Q300 1074 233 1067 Z" fill="var(--ink)"/>
      <path d="M447 1065 Q510 1060 574 1067 Q510 1074 447 1065 Z" fill="var(--ink)"/>
      <polygon fill="var(--ink)" points="404,1031 412,1041 424,1036 425,1048 438,1050 431,1061 440,1070 428,1075 431,1088 418,1087 413,1099 404,1091 395,1099 390,1087 377,1088 380,1075 368,1070 377,1061 370,1050 383,1048 384,1036 396,1041"/>
    </g>
  </svg>

  <h1 class="headline headline--ride">Ride</h1>
  <p class="headline headline--a">a</p>
  <p class="headline headline--tandem">Tandem</p>

  <p class="banner__label">MY BUCKETLIST GOAL</p>

  <p class="badge__label">No<br>18</p>
</main>
</body>
</html>
```